Velmora Outcomes Brochure Design Project

- Who we are?
Velmora Outcomes is New Internet Marketing Company Based in China.

It is our aim to provide Chinese clients with the means to internationally market their product, via the Internet.

Our primary products are Outsourced Design ( Thanks to Pixel hive and the amazing designers who use it), SEO and Virtual Hosting.

- Project Brief
Design a vibrant and fresh brochure that introduces the fundamentals of SEO. There is no restriction to the number of pages, however all the info I have included in this brief must be included.

- Colour Palette
Please see link or download the Adobe Swatch Exchange File or follow the link below
http://tintaro.example.com/#themes/search?term=5830716
Updates

Logo updated - grey background removed

Various file formats added for logo and brochure content

Brochure zip file add containing logo in different formats.

Adobe color scheme file added

The general corporate colors are:

Base Color: CMYK :0, 60, 80, 0  Hex: FF6633
Dark Orange: CMYK: 0, 72, 96, 30 Hex: B23308
Light Orange: CMYK 0, 42, 56, 0 Hex: FF9571
Grey: CMYK 0, 0, 0, 48 Hex: 858585
Light Grey: CMYK 0, 0, 0, 26 Hex: BDBDBD

Please note that I'm happy for other colors to be included, however I would like these the corporate branding colors to be clearly present through the brochure.

Hi All

First place payment has increased to $600 - Looking to see some creative designs!

Hi All

Project Deadline Extended
Reason: I have increase the budget and extend the deadline as I need to see more design.

I have attached a zip file that contains example brochures I like.

We are not keen on the table data its a little plain. We have create an info-graphic to replace one of the table and would like to see it included in the design.

Project Deadline Extended
Reason: A few designers have asked for this extension and I would like to see additional designs. Thanks Marek

Target Market(s)

- Our Target Audience is..
It is small to medium businesses looking to reach out to the international market.
Our clients still very much operate on a face to face level in business and are new to the concept of Internet marketing

However this must look professional, Marketable and Clean, with the power of connecting people globally, through SEO and design to be reflected visually in the brochure.

Industry/Entity Type

Internet

Requirements
Must have
• One or more of the FACTS that I have highlighted need to stand out on each page. These FACTS can be found the document attached to this brief and are under the section titled 'Did You Know!'. Not every fact in this section needs to be highlighted in the brochure, but each page needs to have at least, one or more fact that stands out, soemwhere on the page.
See attached document, under the heading 'Did you Know!' and use one or two of these facts to spruce up the pages!

One image/ per page or per two pages MUST be included!

- Provide stock photos and please send us a message with the additional cost of these with your submission

The Table data, that I have included in the attachment must be included in the body of the pages - BUT the table format is not necessary and you can place the information in the body like plain text.

The brochure size should be a little larger than A4.

Please design the back page, like a pocket to hold paper and other material in it that I include with this brochure.

```html
<!DOCTYPE html>
<html lang="en">
<head>
<meta charset="utf-8">
<title>Velmora Outcomes – Web Design Spread</title>
<link rel="stylesheet" href="https://fonts.googleapis.com/css2?family=Source+Sans+3:wght@400;600;700&display=swap">
<style>
  :root {
    --stage: #2a2a2a;
    --orange: #ff6633;
    --orange-deep: #e4531f;
    --orange-dark: #b23308;
    --orange-light: #f4914c;
    --orange-bar: #f47c3c;
    --grey: #858585;
    --grey-light: #bdbdbd;
    --grey-bar: #c4c4c4;
    --paper: #ffffff;
    --paper-shade: #ececec;
    --teal-dark: #1d4f5a;
    --teal-light: #7ea6ad;
    --ink: #1e1e1e;
    --white: #ffffff;
  }
  * { margin: 0; padding: 0; box-sizing: border-box; }
  html, body {
    width: 1200px; height: 793px; overflow: hidden;
    background: var(--stage);
    font-family: "Source Sans 3", "Myriad Pro", Arial, sans-serif;
  }
  .spread { position: absolute; left: 109px; top: 62px; width: 983px; height: 698px; }
  .page { position: absolute; top: 0; height: 698px; overflow: hidden; }
  .page--left { left: 0; width: 491px; background: linear-gradient(180deg, var(--paper) 20%, var(--paper-shade) 100%); }
  .page--right { left: 491px; width: 492px; background: var(--paper); }

  .headline-band {
    position: absolute; left: 0; top: 0; width: 100%; height: 86px;
    background: linear-gradient(90deg, var(--orange-deep), var(--orange) 60%, #f57a3e);
  }
  .headline {
    position: absolute; left: 37px; top: 29px;
    color: var(--white); font-size: 19.5px; font-weight: 400; line-height: 25px;
    text-transform: uppercase; letter-spacing: 0.1px;
  }
  .headline strong { font-weight: 700; }
  .section-band {
    position: absolute; left: 0; top: 86px; width: 100%; height: 44px;
    background: linear-gradient(90deg, var(--orange-light), #f9a466);
    color: var(--white); padding: 7px 0 0 38px; font-size: 13px; line-height: 17px;
  }
  .section-band .section-title { font-weight: 700; display: block; }
  .section-band .section-sub { text-transform: uppercase; display: block; }

  .chart { position: absolute; left: 0; top: 0; width: 491px; height: 610px; }
  .chart text { font-family: "Source Sans 3", Arial, sans-serif; }
  .axis-label { font-size: 14px; fill: var(--ink); }
  .bar-orange { fill: var(--orange-bar); }
  .bar-grey { fill: var(--grey-bar); }
  .bar-outline { fill: var(--paper); stroke: var(--grey); stroke-width: 1; }
  .bar-tip { fill: var(--orange-dark); }
  .bar-text { font-size: 9px; fill: var(--white); }
  .bar-text--dark { font-size: 8px; fill: var(--ink); }
  .ring { fill: none; stroke: var(--grey-light); stroke-width: 1.5; }
  .scale { stroke: var(--ink); stroke-width: 1; }
  .scale-label { font-size: 7px; fill: var(--ink); }
  .callout { font-size: 10.5px; font-weight: 700; fill: var(--orange); }

  .info-band {
    position: absolute; left: 0; top: 610px; width: 100%; height: 88px;
    background: linear-gradient(90deg, var(--teal-dark), #2f6773 55%, var(--teal-light));
  }
  .clock-photo {
    position: absolute; left: 0; top: 0; width: 123px; height: 88px;
    background: radial-gradient(circle at 60% 60%, #f4f4f4 0%, #d6d6d6 55%, #8a8a8a 100%);
  }
  .info-title {
    position: absolute; left: 131px; top: 7px;
    color: var(--white); font-size: 15px; font-weight: 700; text-transform: uppercase;
  }
  .info-copy {
    position: absolute; left: 131px; top: 24px; width: 355px;
    color: var(--white); font-size: 12.2px; line-height: 14px;
  }

  .top-strip {
    position: absolute; left: 0; top: 0; width: 100%; height: 20px;
    background: linear-gradient(90deg, var(--orange-deep), var(--orange) 50%, #f79a63);
  }
  .hero-photo {
    position: absolute; left: 0; top: 20px; width: 100%; height: 632px;
    background: linear-gradient(180deg, #9fb9c6 0%, #d3dbd6 35%, #e9d6a3 52%, #7c7a4a 66%, #3f4427 100%);
  }
  .bottom-strip {
    position: absolute; left: 0; top: 652px; width: 100%; height: 46px;
    background: linear-gradient(90deg, #3e6f78, var(--teal-light));
  }
</style>
</head>
<body>
<main class="spread">
  <section class="page page--left">
    <header class="headline-band">
      <h1 class="headline">The location of you website/server <strong>makes<br>a difference</strong> to who gets to see it</h1>
    </header>
    <div class="section-band">
      <span class="section-title">WEB DESIGN</span>
      <span class="section-sub">Our method vs traditional</span>
    </div>

    <svg class="chart" viewBox="109 62 491 610" aria-label="Comparison infographic: our design method versus traditional design companies">
      <path class="ring" d="M223.7 574.3 A190 190 0 1 1 522.5 535"/>
      <path class="ring" d="M310.4 467.5 A55 55 0 1 1 400.1 475.4"/>

      <!-- Designers available -->
      <path class="bar-orange" d="M422.9 442.3 L557.8 447 A200 200 0 0 1 551.2 491.8 L420.8 456.8 A65 65 0 0 0 422.9 442.3 Z"/>
      <path class="bar-grey" d="M415.1 458.5 L462.6 474 A110 110 0 0 1 455.1 491.6 L411 468.1 A60 60 0 0 0 415.1 458.5 Z"/>
      <text class="bar-text" transform="translate(475 473) rotate(8)">10000+ Designers</text>
      <text class="bar-text--dark" transform="translate(420 478) rotate(63)"><tspan x="0" y="0">Design</tspan><tspan x="-8" y="9">companies</tspan><tspan x="-6" y="18">have ~1000</tspan></text>
      <text class="axis-label" transform="translate(549 486) rotate(72)">Designers Available</text>

      <!-- Number of revisions -->
      <path class="bar-orange" d="M409.2 400 L507.2 323.7 A190 190 0 0 1 538.7 381.7 L419.8 419.9 A65 65 0 0 0 409.2 400 Z"/>
      <path class="bar-grey" d="M416.2 425.5 L455 415.8 A100 100 0 0 1 457.8 433 L417.9 435.8 A60 60 0 0 0 416.2 425.5 Z"/>
      <text class="bar-text" transform="translate(455 385) rotate(-28)">Unlimited</text>
      <text class="bar-text--dark" transform="translate(462 425) rotate(-8)"><tspan x="0" y="0">2 or 3 revisions</tspan><tspan x="10" y="9">on select</tspan><tspan x="14" y="18">designs</tspan></text>
      <text class="axis-label" transform="translate(524 314) rotate(62)">Number of Revisions</text>

      <!-- Project designers -->
      <path class="bar-orange" d="M371 366.1 L390.2 257.8 A185 185 0 0 1 444.8 276.6 L393.2 373.8 A75 75 0 0 0 371 366.1 Z"/>
      <path class="bar-grey" d="M389.8 389.1 L419 342.5 A115 115 0 0 1 434.9 354.6 L398.1 395.4 A60 60 0 0 0 389.8 389.1 Z"/>
      <text class="bar-text" transform="translate(392 275) rotate(10)">60+</text>
      <text class="bar-text" transform="translate(382 345) rotate(-75)"><tspan x="0" y="0">A large number</tspan><tspan x="6" y="11">of designers</tspan></text>
      <text class="bar-text--dark" transform="translate(418 372) rotate(-62)"><tspan x="0" y="0">Small team of</tspan><tspan x="8" y="9">designers</tspan></text>
      <line class="scale" x1="380" y1="408" x2="432" y2="290"/>
      <text class="scale-label" x="378" y="414">0</text>
      <text class="scale-label" x="430" y="289">60</text>
      <text class="axis-label" transform="translate(394 243) rotate(22)">Project Designers</text>

      <!-- Design variety -->
      <path class="bar-orange" d="M308.2 398.2 L231.6 333.9 A165 165 0 0 1 275.5 297.1 L325.5 383.7 A65 65 0 0 0 308.2 398.2 Z"/>
      <path class="bar-grey" d="M332.6 385.6 L311.5 340.3 A110 110 0 0 1 331.4 333.3 L343.5 381.8 A60 60 0 0 0 332.6 385.6 Z"/>
      <text class="bar-text" transform="translate(266 313) rotate(58)" style="font-size:8px"><tspan x="0" y="0">Many international designers</tspan><tspan x="6" y="10">Many unique designs</tspan></text>
      <text class="bar-text--dark" transform="translate(320 343) rotate(75)" style="font-size:7px"><tspan x="0" y="0">Bunch of</tspan><tspan x="-4" y="8">similar designs</tspan></text>
      <text class="axis-label" transform="translate(232 270) rotate(-20)">Design Variety</text>

      <!-- Designs to choose from -->
      <path class="bar-orange" d="M268.1 443.2 L163.2 446.8 A195 195 0 0 1 174.7 373.3 L273.4 409.2 A90 90 0 0 0 268.1 443.2 Z"/>
      <path class="bar-grey" d="M303.6 414.6 L285.5 406.2 A80 80 0 0 1 290.2 397.6 L307.1 408.2 A60 60 0 0 0 303.6 414.6 Z"/>
      <text class="bar-text" transform="translate(177 420) rotate(-80)">100+</text>
      <text class="bar-text" transform="translate(198 420) rotate(12)"><tspan x="0" y="0">Greatest selection</tspan><tspan x="10" y="11">of designs</tspan></text>
      <text class="bar-text--dark" transform="translate(252 385) rotate(22)"><tspan x="0" y="0" style="font-size:9px">Small group</tspan><tspan x="6" y="10" style="font-size:9px">of designs</tspan></text>
      <line class="scale" x1="185" y1="387" x2="310" y2="437"/>
      <text class="scale-label" x="182" y="385">100</text>
      <text class="scale-label" x="311" y="442">0</text>
      <text class="axis-label" transform="translate(155 440) rotate(-80)">Designs to Choose From</text>

      <!-- Cost saving -->
      <path class="bar-outline" d="M300.9 458.5 L186.8 495.6 A180 180 0 0 1 178.4 452.6 L298.1 444.2 A60 60 0 0 0 300.9 458.5 Z"/>
      <path class="bar-orange" d="M312 478.6 L231.6 546.1 A165 165 0 0 1 202.9 496.4 L301.6 460.5 A60 60 0 0 0 312 478.6 Z"/>
      <path class="bar-tip" d="M312 478.6 L302 487 A73 73 0 0 1 289.6 465 L301.6 460.5 A60 60 0 0 0 312 478.6 Z"/>
      <text class="bar-text--dark" transform="translate(190 468) rotate(-10)" style="font-size:7.5px"><tspan x="0" y="0">Pay for a team of designers,</tspan><tspan x="4" y="9">overhead costs and</tspan><tspan x="8" y="18">unwanted designs</tspan></text>
      <text class="bar-text--dark" transform="translate(284 460) rotate(-8)" style="font-size:6px">shares</text>
      <text class="bar-text" transform="translate(222 528) rotate(-32)" style="font-size:8.5px">You Save on Everything else</text>
      <text class="axis-label" transform="translate(166 521) rotate(102)">Cost Saving</text>

      <!-- callout -->
      <path d="M290 588 Q318 565 320 530" fill="none" stroke="var(--orange-light)" stroke-width="3"/>
      <path d="M313 535 L320 522 L326 536 Z" fill="var(--orange-light)"/>
      <text class="callout" transform="translate(254 595) rotate(-18)"><tspan x="0" y="0">You only pay for this:</tspan><tspan x="2" y="12">your chosen design</tspan></text>
    </svg>

    <div class="info-band">
      <div class="clock-photo" role="img" aria-label="Close-up photo of a white wall clock face"></div>
      <h2 class="info-title">How long does it take?</h2>
      <p class="info-copy">Normally a design project takes between 10 and 15 days… but don’t worry if you are in a rush - we have created projects with amazing results in less than 5 days.</p>
    </div>
  </section>

  <section class="page page--right">
    <div class="top-strip"></div>
    <div class="hero-photo" role="img" aria-label="Photo of a businessman with a laptop running through a sunlit meadow of dandelions"></div>
    <div class="bottom-strip"></div>
  </section>
</main>
</body>
</html>
```